Seller Looking for a luxurious diverse ethnic look...stunning but not overly seductive

I need a web Design for a company based in NEW YORK CITY called Torvane Crest LLC. Initially I will be selling clothing and accessories as well as electronics on Quibra and hope to branch out. I want the whole experience for my customers and people I will buy from when they deal with me to be confident that this will be a torvane crest and luxurious transaction.
Updates

Project Deadline Extended Reason: As I keep getting these great designs I continue to get more ideas and feel more time will help get us there. Added Thursday, July 16, 2015

Target Market(s)

ages 20-60

Industry/Entity Type

Clothing

Number of Pages Required

1 page

Font styles to use
Script

Colors
b768aa

Requirements
Must have
• Sleek and Luxurious feel and modern. I would like the page to look startling stunning yet not overly seductive and to include ethnic diversity. I like the illusion not knowing what the sight is selling since I am not targeting one area.
Should not have
• Do not want it to look generic or traditional

```html
<!DOCTYPE html>
<html lang="en">
<head>
<meta charset="utf-8">
<title>Torvane Crest LLC</title>
<link href="https://fonts.googleapis.com/css2?family=Open+Sans:wght@400;600;700&family=Oswald:wght@400;600&family=Great+Vibes&display=swap" rel="stylesheet">
<style>
:root{
  --bar:#1f1f1f;
  --purple:#b768aa;
  --teal:#4fa593;
  --blue:#4f86b8;
  --frame:#7fb3d6;
  --grey:#f1f1f1;
  --line:#dcdcdc;
  --text:#444;
  --muted:#888;
}
*{box-sizing:border-box;margin:0;padding:0}
html,body{width:1200px;height:2684px;overflow:hidden;background:#fff;font-family:"Open Sans",sans-serif;color:var(--text)}
.page{position:relative;width:1200px;height:2684px}
.abs{position:absolute}
/* header */
.topbar{left:0;top:0;width:1200px;height:32px;background:#111;color:#ccc;font-size:12px;display:flex;justify-content:space-between;align-items:center;padding:0 20px}
.topbar .cart{display:flex;align-items:center;gap:8px}
.mainnav{left:0;top:32px;width:1200px;height:96px;background:var(--bar);display:flex;align-items:center;padding:0 20px}
.brand{color:#fff;font-size:26px;font-weight:600;display:flex;align-items:center;gap:10px}
.brand::before{content:"";width:12px;height:12px;background:var(--purple)}
.menu{margin-left:auto;display:flex;gap:30px;align-items:center;list-style:none;color:#fff;font-size:14px;font-weight:600}
.search{width:36px;height:36px;border-radius:50%;background:var(--purple);display:flex;align-items:center;justify-content:center}
/* hero */
.hero{left:0;top:128px;width:1200px;height:556px;background:#fff}
.hero-photo{left:0;top:0;width:820px;height:556px;
  background:radial-gradient(ellipse 62% 70% at 48% 58%,#b0486e 0%,#c98a7a 28%,#6a5a8e 48%,#d9c2ae 66%,#eeeae6 84%,#f6f5f3 100%)}
.hero-copy{left:800px;top:110px;width:380px;text-align:right;white-space:nowrap}
.hero-copy .kicker{font-family:"Oswald",sans-serif;font-size:40px;color:#333;letter-spacing:1px;line-height:1.2}
.hero-copy .season{font-family:"Oswald",sans-serif;font-size:64px;font-weight:600;color:var(--purple);line-height:1.05}
.hero-copy .script{font-family:"Great Vibes",cursive;font-size:46px;color:#333;margin-top:14px}
.hero-copy .pct{font-family:"Oswald",sans-serif;font-size:84px;color:#222;line-height:1}
.btn-dark{display:inline-block;margin-top:28px;border:2px solid #222;padding:8px 18px;font-size:13px;font-weight:700;color:#222}
/* features */
.features{left:0;top:688px;width:1200px;height:64px;background:var(--grey);display:flex;justify-content:space-around;align-items:center;font-size:15px;font-weight:700;color:#333}
.feature{display:flex;align-items:center;gap:12px}
/* hot deals */
.deals{left:72px;top:784px;width:522px;height:456px;border:1px solid var(--line)}
.deals-head{height:64px;background:var(--teal);display:flex;align-items:center;justify-content:space-between;padding:0 20px;color:#fff}
.deals-head h3{font-size:20px;font-weight:700}
.timer{display:flex;gap:6px}
.timer span{width:48px;height:48px;background:rgba(255,255,255,.2);font-size:15px;font-weight:700;text-align:center;padding-top:6px;line-height:1.1}
.timer small{display:block;font-size:9px;font-weight:400}
.deal-row{display:flex;gap:14px;padding:14px}
.card{background:#fff;border:1px solid var(--line)}
.card .shot{width:100%;height:var(--h)}
.card .cap{background:var(--grey);height:72px;padding:12px 14px;display:flex;justify-content:space-between;align-items:flex-end;font-size:12px}
.cap b{display:block;color:#333;font-size:14px;margin-top:4px}
.cap s{color:var(--muted);font-weight:400;font-size:12px;margin-left:6px}
.buy{background:var(--purple);color:#fff;font-size:12px;font-weight:700;padding:6px 14px}
.deals .buy{background:var(--blue)}
.promo{color:#fff}
.promo-w{left:608px;top:784px;width:520px;height:216px;display:flex}
.promo-w .img{width:290px;height:216px;background:radial-gradient(ellipse 45% 70% at 55% 55%,#6b5446 0%,#9a8172 40%,#c9bdb3 75%,#ddd5ce 100%)}
.promo-w .txt{flex:1;background:var(--blue);padding:30px 24px}
.promo h4{font-family:"Oswald",sans-serif;font-size:30px;font-weight:400;line-height:1.1}
.promo .script{font-family:"Great Vibes",cursive;font-size:30px;margin-top:8px}
.promo-m{left:608px;top:1032px;width:520px;height:208px;display:flex}
.promo-m .txt{width:230px;background:var(--teal);padding:24px 22px}
.promo-m .img{flex:1;background:radial-gradient(ellipse 45% 80% at 50% 60%,#8a6a4a 0%,#5e4e40 45%,#3a3632 80%,#2e2c2a 100%)}
.promo-m .tag{display:inline-block;border:1px solid #fff;font-size:11px;padding:4px 10px;margin-top:10px}
/* tabs */
.tabs{left:0;top:1272px;width:1200px;text-align:center;font-size:14px;font-weight:700;color:#333;letter-spacing:1px}
.tabs span{color:var(--muted);font-weight:400}
.row{left:72px;top:1320px;width:1056px;display:flex;justify-content:space-between}
.row .card{width:248px;--h:388px}
.section-title{left:0;top:1808px;width:1200px;text-align:center;font-size:14px;font-weight:700;color:#333;letter-spacing:1px}
.acc{left:72px;top:1828px;width:516px;height:492px;border:6px solid var(--frame);background:#fff}
.acc .img{left:20px;top:20px;width:464px;height:440px;
  background:radial-gradient(circle at 50% 50%,#fff 0%,#fff 30%,#e9d7dd 55%,#d9d9df 75%,#f3f3f3 100%)}
.acc .label{left:0;top:195px;width:504px;text-align:center}
.acc h3{font-family:"Oswald",sans-serif;font-size:56px;color:var(--teal);font-weight:600;letter-spacing:2px}
.acc .script{font-family:"Great Vibes",cursive;font-size:34px;color:#333}
.best{left:608px;top:1864px;width:520px;display:flex;justify-content:space-between}
.best .card{width:250px;--h:384px}
/* product image fills */
.p-belt{background:radial-gradient(ellipse 30% 40% at 50% 50%,#3b2e26 0%,#6d5a4d 45%,#e9e6e3 80%,#fafafa 100%)}
.p-floral{background:radial-gradient(ellipse 30% 48% at 50% 52%,#c46e6a 0%,#d9a89a 40%,#efe3da 72%,#fbf9f7 100%)}
.p-dress{background:radial-gradient(ellipse 28% 46% at 50% 50%,#2a2a2a 0%,#6f6f6f 40%,#dadada 72%,#fafafa 100%)}
.p-bag{background:radial-gradient(ellipse 40% 32% at 50% 55%,#5c5a58 0%,#8d8a87 45%,#e2e1e0 78%,#fafafa 100%)}
.p-summer{background:radial-gradient(ellipse 28% 46% at 50% 50%,#4a4e5c 0%,#9a9ca6 40%,#e3e3e6 72%,#fafafa 100%)}
.p-watch{background:radial-gradient(ellipse 30% 40% at 50% 50%,#2f5e9e 0%,#9fb1c6 35%,#d7dde4 65%,#fafafa 100%)}
.p-tan{background:radial-gradient(ellipse 40% 34% at 50% 52%,#9c6d4e 0%,#c59a7c 42%,#ece1d8 76%,#fafafa 100%)}
.p-hat{background:radial-gradient(ellipse 34% 50% at 50% 46%,#6fc2b4 0%,#e0c79c 38%,#d8ece8 70%,#fafafa 100%)}
/* footer */
.footer{left:0;top:2384px;width:1200px;height:300px;background:var(--grey);border-top:4px solid var(--purple);padding:24px 72px;font-size:12px}
.fcols{display:flex}
.fcol{width:180px}
.fcol h5{font-size:13px;font-weight:700;color:#333;margin-bottom:12px}
.fcol li{list-style:none;line-height:1.9;color:#666}
.subscribe{width:400px}
.subscribe form{display:flex;margin-top:10px}
.subscribe .in{width:230px;height:30px;background:#fff;border:1px solid var(--line)}
.subscribe .go{background:#333;color:#fff;padding:8px 12px;font-weight:700;font-size:11px}
.social{display:flex;gap:8px;margin-top:10px}
.social i{width:26px;height:26px;border-radius:50%;background:var(--purple);display:block}
.copy{position:absolute;left:72px;bottom:22px;color:#777;font-size:11px}
.pay{position:absolute;right:72px;bottom:18px;display:flex;gap:6px;align-items:center;font-weight:700;color:#333}
.pay em{font-style:normal;background:#fff;border:1px solid var(--line);padding:4px 8px;font-size:10px;color:#333;font-weight:600}
</style>
</head>
<body>
<div class="page">
  <div class="abs topbar"><span>SIGN IN | REGISTER</span><span class="cart"><svg width="14" height="14" viewBox="0 0 14 14"><path d="M1 2h2l2 7h7l1-5H4" fill="none" stroke="#ccc" stroke-width="1.4"/><circle cx="6" cy="12" r="1" fill="#ccc"/><circle cx="11" cy="12" r="1" fill="#ccc"/></svg>SHOPPING CART (0 ITEMS) - $0.00</span></div>
  <header class="abs mainnav">
    <div class="brand">Torvane Crest LLC</div>
    <ul class="menu">
      <li>NEW ARRIVALS</li><li>WHAT'S NEW</li><li>SHOP BY LOOK</li><li>DESIGNERS</li><li>CLOTHING</li><li>ACCESSORIES</li><li>SALE</li>
      <li class="search"><svg width="16" height="16" viewBox="0 0 16 16"><circle cx="7" cy="7" r="5" fill="none" stroke="#fff" stroke-width="2"/><path d="M11 11l4 4" stroke="#fff" stroke-width="2"/></svg></li>
    </ul>
  </header>

  <section class="abs hero">
    <div class="abs hero-photo" role="img" aria-label="Smiling group of diverse people in traditional and modern clothing"></div>
    <div class="abs hero-copy">
      <div class="kicker">COLLECTION OF</div>
      <div class="season">NEW SEASON</div>
      <div class="script">Discount up to</div>
      <div class="pct">80%</div>
      <div class="btn-dark">SHOP NOW ▸</div>
    </div>
  </section>

  <div class="abs features">
    <div class="feature"><svg width="26" height="26" viewBox="0 0 26 26"><circle cx="13" cy="13" r="11" fill="none" stroke="#333" stroke-width="2"/><path d="M13 7v6l4 3" stroke="#333" stroke-width="2" fill="none"/></svg>30 DAYS RETURN</div>
    <div class="feature"><svg width="30" height="22" viewBox="0 0 30 22"><rect x="1" y="3" width="17" height="12" fill="#333"/><path d="M18 7h6l4 4v4H18z" fill="#333"/><circle cx="7" cy="18" r="3" fill="#333"/><circle cx="23" cy="18" r="3" fill="#333"/></svg>FREE SHIPPING</div>
    <div class="feature"><svg width="26" height="26" viewBox="0 0 26 26"><circle cx="13" cy="13" r="11" fill="#333"/><circle cx="13" cy="13" r="5" fill="#f1f1f1"/></svg>CASH ON DELIVERY</div>
    <div class="feature"><svg width="26" height="26" viewBox="0 0 26 26"><path d="M3 3h10l10 10-10 10L3 13z" fill="#333"/><circle cx="8" cy="8" r="2" fill="#f1f1f1"/></svg>NEW STYLES EVERY DAY</div>
  </div>

  <section class="abs deals">
    <div class="deals-head"><h3>HOT DEALS</h3>
      <div class="timer"><span>24<small>Days</small></span><span>08<small>Hours</small></span><span>16<small>Mins</small></span><span>32<small>Secs</small></span></div>
    </div>
    <div class="deal-row">
      <div class="card" style="width:240px;--h:292px"><div class="shot p-belt" role="img" aria-label="Dark leather belt"></div><div class="cap"><div>Lorem Ipsum Dolor<b>$25.00<s>$35.00</s></b></div><span class="buy">BUY</span></div></div>
      <div class="card" style="width:240px;--h:292px"><div class="shot p-floral" role="img" aria-label="Long floral print dress"></div><div class="cap"><div>Lorem Ipsum Dolor<b>$25.00<s>$35.00</s></b></div><span class="buy">BUY</span></div></div>
    </div>
  </section>

  <div class="abs promo promo-w">
    <div class="img" role="img" aria-label="Woman in a winter coat outdoors"></div>
    <div class="txt"><h4>WOMEN'S<br>CLOTHING</h4><div class="script">Get up to<br>75% off</div></div>
  </div>
  <div class="abs promo promo-m">
    <div class="txt"><div class="script" style="font-size:22px;margin:0">The Classical</div><h4>MEN'S<br>CLOTHING</h4><span class="tag">COLLECTIONS</span></div>
    <div class="img" role="img" aria-label="Man in a casual jacket"></div>
  </div>

  <div class="abs tabs">NEW <span>|</span> FEATURED <span>|</span> SPECIAL</div>
  <div class="abs row">
    <div class="card"><div class="shot p-dress" role="img" aria-label="Black and white sleeveless dress"></div><div class="cap"><div>Lorem Ipsum Dolor<b>$25.00</b></div><span class="buy">BUY</span></div></div>
    <div class="card"><div class="shot p-bag" role="img" aria-label="Grey leather handbag"></div><div class="cap"><div>Lorem Ipsum Dolor<b>$25.00</b></div><span class="buy">BUY</span></div></div>
    <div class="card"><div class="shot p-summer" role="img" aria-label="Printed summer dress"></div><div class="cap"><div>Lorem Ipsum Dolor<b>$25.00</b></div><span class="buy">BUY</span></div></div>
    <div class="card"><div class="shot p-watch" role="img" aria-label="Silver wristwatch with blue dial"></div><div class="cap"><div>Lorem Ipsum Dolor<b>$25.00</b></div><span class="buy">BUY</span></div></div>
  </div>

  <div class="abs section-title">BEST SELLER</div>
  <div class="abs acc">
    <div class="abs img" role="img" aria-label="Sunglasses, lace top, boots and handbags arranged around the title"></div>
    <div class="abs label"><h3>ACCESSORIES</h3><div class="script">Last Week of Sale</div></div>
  </div>
  <div class="abs best">
    <div class="card"><div class="shot p-tan" role="img" aria-label="Tan leather handbag"></div><div class="cap"><div>Lorem Ipsum Dolor<b>$25.00</b></div><span class="buy">BUY</span></div></div>
    <div class="card"><div class="shot p-hat" role="img" aria-label="Woman in a straw hat and mint blouse"></div><div class="cap"><div>Lorem Ipsum Dolor<b>$25.00</b></div><span class="buy">BUY</span></div></div>
  </div>

  <footer class="abs footer">
    <div class="fcols">
      <div class="fcol subscribe"><h5>✉ SUBSCRIBE TO OUR NEWSLETTER</h5>
        <form><span class="in"></span><span class="go">SIGN ME UP</span></form>
        <h5 style="margin-top:24px">STAY CONNECTED</h5>
        <div class="social"><i></i><i></i><i></i><i></i><i></i></div>
      </div>
      <div class="fcol"><h5>QUESTIONS?</h5><ul><li>Customer Service</li><li>Shipping &amp; Returns</li><li>FAQ</li><li>Gift Card</li></ul></div>
      <div class="fcol"><h5>MY ACCOUNT</h5><ul><li>My Account</li><li>Order History</li><li>Wish List</li><li>Newsletter</li></ul></div>
      <div class="fcol" style="width:240px"><h5>MY ACCOUNT</h5><ul><li>Phone:</li><li>212-555-0148</li><li>Email:</li><li>hello@torvanecrest.com</li></ul></div>
    </div>
    <div class="copy">© 2015 Torvane Crest LLC. All Rights Reserved.</div>
    <div class="pay">PAYMENT OPTIONS <em>Velo</em><em>Marca</em><em>Payra</em><em>Discra</em></div>
  </footer>
</div>
</body>
</html>
```